Web Design for Rubbish Removal Company

I am looking for a custom web design that is clean and modern which also has a professional trustworthy feel to it.
The website is http://www.tidlowhaulage.com.au/ and need:
1 x Front Page
1 x Location Page
Please keep the green colour scheme as this is the corporate colours but would like to steer away from the black.
Industry/Entity Type
It Company
Number of Pages Required
2 page
Font styles to use
Sans Serif
Requirements
Must have
- Clean & Professional
- Keep green colour scheme
Should not have
- Steer away from black
- not look like a template

```html
<!DOCTYPE html>
<html lang="en">
<head>
<meta charset="utf-8">
<title>Tidlow Rubbish Removal</title>
<link href="https://fonts.googleapis.com/css2?family=Montserrat:wght@400;600;700;800&family=Open+Sans:wght@400;600;700&display=swap" rel="stylesheet">
<style>
:root{
  --green:#7cc242;
  --green-dark:#5f9e2c;
  --ink:#2d2d2d;
  --charcoal:#2f3033;
  --charcoal-2:#3a3b3e;
  --grey:#6f6f6f;
  --light:#f1f2f2;
  --line:#d9d9d9;
  --white:#ffffff;
}
*{box-sizing:border-box;margin:0;padding:0}
html,body{width:1200px;height:4356px;overflow:hidden}
body{font-family:"Open Sans",Arial,sans-serif;color:var(--ink);background:var(--white);font-size:14px;line-height:1.6}
h1,h2,h3,h4,.btn,.nav a,.logo{font-family:"Montserrat",Arial,sans-serif}
.wrap{width:1040px;margin:0 auto;position:relative}
.btn{display:inline-block;background:var(--green);color:var(--white);font-weight:700;font-size:13px;text-transform:uppercase;padding:11px 24px;border-radius:3px;letter-spacing:.5px}
.btn-dark{background:var(--ink)}
.accent{color:var(--green)}
.section-title{font-size:30px;font-weight:800;text-transform:uppercase;text-align:center;letter-spacing:.5px}
.title-rule{width:60px;height:3px;background:var(--green);margin:12px auto 0}

/* header */
.site-header{height:130px}
.site-header .wrap{height:130px;display:flex;align-items:center;justify-content:space-between}
.logo{display:flex;align-items:center;gap:12px;font-size:30px;font-weight:800;color:var(--ink);text-transform:uppercase;letter-spacing:-.5px}
.logo-dot{width:22px;height:22px;background:var(--green);border-radius:50%}
.header-contact{display:flex;align-items:center;gap:24px}
.call{display:flex;align-items:center;gap:12px}
.call small{display:block;font-size:11px;color:var(--green);font-weight:700;text-transform:uppercase;line-height:1}
.call strong{font-family:"Montserrat",sans-serif;font-size:20px;font-weight:700;line-height:1.3}

/* nav */
.main-nav{height:42px}
.main-nav ul{list-style:none;display:flex;justify-content:space-between;background:var(--green);height:42px;align-items:center;padding:0 34px}
.nav a{color:var(--white);font-size:12px;font-weight:700;text-transform:uppercase;text-decoration:none}

/* hero */
.hero{height:510px;background:linear-gradient(180deg,#eef0f0,#dfe3e4);position:relative;overflow:hidden}
.hero-photo{position:absolute;left:80px;top:0;width:460px;height:510px;background:linear-gradient(160deg,#cfd8df,#8fb0c8 55%,#5d88b5)}
.hero-copy{position:absolute;right:80px;top:140px;width:560px;text-align:right}
.hero-copy h1{font-size:40px;font-weight:700;color:var(--ink);line-height:1.2}
.hero-copy .btn{margin-top:24px}
.slider-arrows{position:absolute;right:80px;top:330px;display:flex;gap:6px}
.slider-arrows span{width:26px;height:26px;border-radius:50%;background:var(--ink);display:flex;align-items:center;justify-content:center}

/* welcome */
.welcome{height:428px;padding-top:98px}
.welcome .wrap{display:flex;gap:40px}
.welcome-photo{width:260px;height:200px;background:linear-gradient(150deg,#b8c7a6,#7e9a6a 60%,#4f6a45);flex:none}
.welcome-copy h2{font-size:26px;font-weight:800;text-transform:uppercase}
.welcome-copy p{font-size:13px;color:var(--grey);margin:14px 0 20px;line-height:1.75}

/* services */
.services{height:610px;background:linear-gradient(180deg,#3d3e40,#2a2b2d);color:var(--white);padding-top:70px}
.services .section-title{color:var(--white)}
.service-cards{display:flex;gap:22px;margin-top:44px}
.service-card{flex:1;background:var(--white);color:var(--ink);padding:10px;}
.service-card h3{font-size:13px;font-weight:800;text-transform:uppercase;padding:2px 0 8px}
.service-card .thumb{height:130px}
.service-card p{background:var(--green);color:var(--white);font-size:12px;line-height:1.5;padding:12px 12px;margin:0 -10px -10px}
.price-line{text-align:center;margin-top:48px}
.price-line h3{font-size:20px;font-weight:800;text-transform:uppercase}
.price-phone{display:flex;justify-content:center;align-items:center;gap:12px;margin-top:14px;font-family:"Montserrat",sans-serif;font-size:30px;font-weight:700;color:var(--green)}

/* why */
.why{height:470px;padding-top:70px}
.why .lead{text-align:center;font-weight:700;font-size:15px;margin-top:28px}
.reasons{display:flex;justify-content:space-between;margin-top:54px;padding:0 60px}
.reason{width:190px;text-align:center;font-size:14px;color:var(--ink);line-height:1.4}
.reason svg{display:block;margin:0 auto 18px}

/* blogs */
.blogs{height:530px;background:linear-gradient(180deg,#3a3b3d,#2b2c2e);color:var(--white);padding-top:70px}
.blogs .section-title{color:var(--white)}
.blog-list{display:flex;gap:40px;margin:46px 0 0 0;padding:0 40px 0 0}
.blog{flex:1;display:flex;background:var(--white);color:var(--ink);height:240px;position:relative}
.blog .thumb{width:230px;flex:none}
.blog .date{position:absolute;left:200px;top:60px;width:56px;background:var(--green);color:var(--white);text-align:center;font-family:"Montserrat",sans-serif;font-weight:700;line-height:1.1;padding:8px 0}
.blog .date b{display:block;font-size:22px}
.blog .body{padding:24px 20px 20px 40px}
.blog h4{font-size:15px;font-weight:700;color:var(--green);line-height:1.3}
.blog p{font-size:12px;color:var(--grey);margin:10px 0;line-height:1.6}
.blog .more{font-size:12px;font-weight:700;color:var(--ink);text-decoration:underline}
.dots{display:flex;justify-content:center;gap:8px;margin-top:30px}
.dots span{width:10px;height:10px;border-radius:50%;background:#6d6e70}
.dots span.on{background:var(--green)}

/* enquiry */
.enquire{height:530px;position:relative}
.enquire .wrap{padding-top:70px}
.enquire h2{font-size:30px;font-weight:800;text-transform:uppercase;line-height:1.25;width:620px}
.enquire .intro{font-size:13px;color:var(--grey);width:620px;margin:16px 0 20px}
.enquiry-form{width:620px;display:grid;grid-template-columns:1fr 1fr;gap:14px 20px}
.field{border:1px solid var(--line);height:42px;font-size:13px;color:var(--grey);padding:10px 14px}
.field.message{grid-column:2;grid-row:1/4;height:auto}
.enquiry-form .btn{grid-column:1;width:120px;text-align:center}
.enquire-photo{position:absolute;right:80px;top:0;width:360px;height:530px;background:linear-gradient(180deg,#e6e8ea,#b7bcc2 60%,#6d737a)}

/* location & testimonials */
.location-testimonials{height:490px;display:flex}
.location{width:490px;background:var(--green);padding:50px 0 0 80px;position:relative}
.location h2,.testimonials h2{font-size:30px;font-weight:800;text-transform:uppercase;color:var(--white)}
.location h2 span{color:var(--ink)}
.location-map{margin-top:30px;width:360px;height:330px;background:linear-gradient(140deg,#f2d27a,#e79a4c 45%,#8fb6d8)}
.testimonials{flex:1;background:var(--charcoal);padding:50px 80px 0 40px;color:var(--white)}
.testimonials h2 span{color:var(--green)}
.client{display:flex;align-items:center;gap:16px;margin-top:44px}
.client-photo{width:60px;height:60px;background:linear-gradient(180deg,#c9c9c9,#7a7a7a)}
.client strong{font-size:14px}
.quote{margin-top:24px;border:1px solid #55575b;padding:24px 28px 24px 70px;position:relative;font-size:13px;color:#c8c9cb;line-height:1.7}
.quote::before{content:"\201C";position:absolute;left:22px;top:4px;font-size:60px;color:var(--green);font-family:Georgia,serif}

/* cta */
.cta{height:250px;text-align:center;padding-top:62px}
.cta h3{font-size:27px;font-weight:800;text-transform:uppercase;line-height:1.35}
.cta .btn{margin-top:20px}

/* footer */
.site-footer{height:366px;background:var(--charcoal-2);color:#cfd0d2;position:relative}
.footer-cols{display:flex;gap:40px;padding-top:40px}
.footer-col h4{font-size:14px;font-weight:800;text-transform:uppercase;color:var(--white);margin-bottom:16px}
.footer-col h4 span{color:var(--green)}
.footer-col ul{list-style:none;font-size:12px;line-height:1.75}
.footer-col li:first-child{color:var(--green)}
.links{width:170px}.contact{width:250px}.map{width:300px}.social{flex:1}
.contact p{font-size:12px;line-height:1.7}
.contact .row{display:flex;gap:10px;align-items:center;font-size:12px;margin-top:8px}
.footer-map{width:280px;height:180px;background:linear-gradient(135deg,#c9d6e0,#9fb7c9 55%,#e6e0cf)}
.social-item{display:flex;align-items:center;gap:12px;font-size:12px;margin-bottom:12px}
.social-item i{width:30px;height:30px;border-radius:50%;background:var(--green);display:block}
.copyright{position:absolute;left:0;right:0;bottom:0;height:44px;background:#2a2b2e;text-align:center;font-size:11px;line-height:44px;color:#9b9c9e}
</style>
</head>
<body>

<header class="site-header">
  <div class="wrap">
    <div class="logo"><span class="logo-dot"></span>Tidlow Rubbish Removal</div>
    <div class="header-contact">
      <div class="call">
        <svg width="34" height="34" viewBox="0 0 34 34"><circle cx="17" cy="17" r="16" fill="none" stroke="#2d2d2d" stroke-width="2"/><path d="M12 10c1-1 2-1 3 0l2 3c.5 1 0 2-1 2.5 1 2 2.5 3.5 4.5 4.5.5-1 1.5-1.5 2.5-1l3 2c1 1 1 2 0 3-2 2-5 1-8-2s-7-7-6-12z" fill="#2d2d2d"/></svg>
        <div><small>Call us now</small><strong>(02) 5550 1842</strong></div>
      </div>
      <span class="btn btn-dark">Get a Quote</span>
    </div>
  </div>
</header>

<nav class="main-nav">
  <div class="wrap">
    <ul class="nav">
      <li><a>Home</a></li><li><a>About Us</a></li><li><a>Services</a></li><li><a>Gallery</a></li><li><a>FAQs</a></li><li><a>Testimonials</a></li><li><a>Location</a></li><li><a>Blog</a></li><li><a>Contact Us</a></li>
    </ul>
  </div>
</nav>

<section class="hero">
  <div class="hero-photo" role="img" aria-label="Three smiling cleaning staff in blue aprons standing together"></div>
  <div class="hero-copy">
    <h1>Sydney's Cheapest Rubbish Removal Services</h1>
    <span class="btn">Contact Now</span>
  </div>
  <div class="slider-arrows">
    <span><svg width="10" height="10" viewBox="0 0 10 10"><path d="M7 1L3 5l4 4" stroke="#fff" stroke-width="2" fill="none"/></svg></span>
    <span><svg width="10" height="10" viewBox="0 0 10 10"><path d="M3 1l4 4-4 4" stroke="#fff" stroke-width="2" fill="none"/></svg></span>
  </div>
</section>

<section class="welcome">
  <div class="wrap">
    <div class="welcome-photo" role="img" aria-label="Cleaners tidying a bright office space"></div>
    <div class="welcome-copy">
      <h2>Welcome to Tidlow <span class="accent">Rubbish</span> Removal</h2>
      <p>Tidlow Rubbish offers complete rubbish removal services for your home or business, including residential households, offices, retail locations, building sites, demolition and more. We are a trusted Sydney rubbish removal company that handles the most demanding work, and we ensure that your rubbish is always recycled or removed responsibly. Our team of professional and friendly rubbish removalists is Sydney-wide and on time.</p>
      <span class="btn">Know More</span>
    </div>
  </div>
</section>

<section class="services">
  <div class="wrap">
    <h2 class="section-title">Our <span class="accent">Services</span></h2>
    <div class="title-rule"></div>
    <div class="service-cards">
      <article class="service-card">
        <h3>Residential Homes</h3>
        <div class="thumb" role="img" aria-label="Suburban house with front lawn" style="background:linear-gradient(180deg,#a9c6e2,#8aa36c)"></div>
        <p>Do you have rubbish slowly building up at home? Quickly clearing out all types of household waste.</p>
      </article>
      <article class="service-card">
        <h3>Commercial Buildings</h3>
        <div class="thumb" role="img" aria-label="Modern commercial office building" style="background:linear-gradient(180deg,#b7c7d6,#6b7f93)"></div>
        <p>Most companies are often busy improving business practices and taking care of staff.</p>
      </article>
      <article class="service-card">
        <h3>Construction Sites</h3>
        <div class="thumb" role="img" aria-label="Worker removing debris at a construction site" style="background:linear-gradient(180deg,#d9c09a,#8a6a4a)"></div>
        <p>Construction and demolition materials usually consist of heavy items, timber.</p>
      </article>
      <article class="service-card">
        <h3>Deceased Estates</h3>
        <div class="thumb" role="img" aria-label="Hands joined in comfort" style="background:linear-gradient(180deg,#c9a98a,#6f8a4f)"></div>
        <p>Losing someone close in the family is always hard, no matter what the circumstances.</p>
      </article>
    </div>
    <div class="price-line">
      <h3>Best prices in Sydney - Grab a free quote with Tidlow Rubbish today by calling</h3>
      <div class="price-phone">
        <svg width="32" height="32" viewBox="0 0 34 34"><circle cx="17" cy="17" r="15" fill="none" stroke="#7cc242" stroke-width="2.5"/><path d="M12 10c1-1 2-1 3 0l2 3c.5 1 0 2-1 2.5 1 2 2.5 3.5 4.5 4.5.5-1 1.5-1.5 2.5-1l3 2c1 1 1 2 0 3-2 2-5 1-8-2s-7-7-6-12z" fill="#7cc242"/></svg>
        0491 570 156
      </div>
    </div>
  </div>
</section>

<section class="why">
  <div class="wrap">
    <h2 class="section-title">Why <span class="accent">Choose Us?</span></h2>
    <div class="title-rule"></div>
    <p class="lead">Complete rubbish clean-out including demolition, strip outs and labour hire</p>
    <div class="reasons">
      <div class="reason">
        <svg width="56" height="64" viewBox="0 0 56 64"><rect x="10" y="16" width="36" height="42" rx="3" fill="#2d2d2d"/><rect x="6" y="9" width="44" height="7" rx="2" fill="#7cc242"/><circle cx="16" cy="60" r="4" fill="#2d2d2d"/><circle cx="40" cy="60" r="4" fill="#2d2d2d"/></svg>
        Removal of white goods, garden rubbish, furniture
      </div>
      <div class="reason">
        <svg width="64" height="64" viewBox="0 0 64 64"><path d="M32 8v46M14 54h36M10 18h44" stroke="#2d2d2d" stroke-width="4" fill="none"/><path d="M4 38l8-20 8 20z" fill="#7cc242"/><path d="M44 38l8-20 8 20z" fill="#7cc242"/></svg>
        No job is too large, too small or too difficult
      </div>
      <div class="reason">
        <svg width="64" height="64" viewBox="0 0 64 64"><path d="M6 32L32 6h24v24L30 56z" fill="#2d2d2d"/><circle cx="46" cy="16" r="5" fill="#7cc242"/></svg>
        Extra discounts for returning customers
      </div>
      <div class="reason">
        <svg width="64" height="64" viewBox="0 0 64 64"><rect x="12" y="6" width="40" height="52" rx="3" fill="#2d2d2d"/><path d="M22 32l8 8 14-16" stroke="#7cc242" stroke-width="5" fill="none"/></svg>
        Free quote provided with all enquiries
      </div>
    </div>
  </div>
</section>

<section class="blogs">
  <div class="wrap">
    <h2 class="section-title">Latest <span class="accent">Blogs</span></h2>
    <div class="title-rule"></div>
    <div class="blog-list">
      <article class="blog">
        <div class="thumb" role="img" aria-label="Pile of broken timber and debris" style="background:linear-gradient(150deg,#d1a878,#8b5e3a)"></div>
        <div class="date"><b>28</b>Nov</div>
        <div class="body">
          <h4>How to Work Safely in the Summer Heat</h4>
          <p>Like summer season approaches, so does the risk of working in an outdoor environment. Long hours in direct sun call for care.</p>
          <a class="more">Read More</a>
        </div>
      </article>
      <article class="blog">
        <div class="thumb" role="img" aria-label="Brick house with cleared rubbish outside" style="background:linear-gradient(150deg,#b9c3cc,#7b6a5d)"></div>
        <div class="date"><b>26</b>Nov</div>
        <div class="body">
          <h4>Top 5 Tips On How To Keep Your Office Clean</h4>
          <p>It is always recommended to keep your office tidy and clean since it can often serve as a first impression for your visitors.</p>
          <a class="more">Read More</a>
        </div>
      </article>
    </div>
    <div class="dots"><span class="on"></span><span></span><span></span></div>
  </div>
</section>

<section class="enquire">
  <div class="enquire-photo" role="img" aria-label="Businessman in a suit giving a thumbs up"></div>
  <div class="wrap">
    <h2>Enquire now and receive a call back within <span class="accent">60 Minutes!</span></h2>
    <p class="intro">Tidlow Rubbish offers some of the best prices in Sydney. We provide an unrivalled, friendly and affordable same-day rubbish clean out to all suburbs in Sydney.</p>
    <div class="enquiry-form">
      <div class="field">Name</div>
      <div class="field message">Message</div>
      <div class="field">Email</div>
      <div class="field">Phone</div>
      <span class="btn">Submit</span>
    </div>
  </div>
</section>

<section class="location-testimonials">
  <div class="location">
    <h2><span>Our</span> Location</h2>
    <div class="location-map" role="img" aria-label="Coloured map of Sydney service areas"></div>
  </div>
  <div class="testimonials">
    <h2>Client <span>Testimonials</span></h2>
    <div class="client">
      <div class="client-photo" role="img" aria-label="Client portrait"></div>
      <strong>Mr. Evan Harlow</strong>
    </div>
    <div class="quote">The team arrived on time, cleared our whole garage in under two hours and left the driveway spotless. Friendly staff, a fair price and a quick response to our enquiry. We will gladly use them again next time and recommend them to all our neighbours.</div>
  </div>
</section>

<section class="cta">
  <div class="wrap">
    <h3>Best prices in Sydney grab a free quote with Tidlow<br>Rubbish today by calling 0491 570 156.</h3>
    <span class="btn">Get a Quote</span>
  </div>
</section>

<footer class="site-footer">
  <div class="wrap footer-cols">
    <div class="footer-col links">
      <h4>Quick <span>Links</span></h4>
      <ul><li>Home</li><li>About Us</li><li>Services</li><li>Gallery</li><li>FAQs</li><li>Testimonials</li><li>Location</li><li>Blog</li><li>Contact Us</li></ul>
    </div>
    <div class="footer-col contact">
      <h4>Contact <span>Details</span></h4>
      <p><strong style="color:#fff">Tidlow Rubbish Removal</strong><br>Fast and reliable rubbish<br>removal across Sydney<br>for over 10 years<br>Monday through to Sunday</p>
      <div class="row"><svg width="14" height="14" viewBox="0 0 14 14"><path d="M3 1c1-1 2 0 2.5 1l1 2c0 1-1 1.5-1 1.5 1 1.5 2 2.5 3 3 0 0 .5-1 1.5-1l2 1c1 .5 1.5 1.5.5 2.5-1.5 1.5-4 1-7-2S1.5 2.5 3 1z" fill="#7cc242"/></svg>0491 570 156</div>
      <div class="row"><svg width="14" height="12" viewBox="0 0 14 12"><rect x="0" y="1" width="14" height="10" fill="#7cc242"/><path d="M0 1l7 5 7-5" stroke="#3a3b3e" fill="none"/></svg>mail@tidlowhaulage.com.au</div>
    </div>
    <div class="footer-col map">
      <h4>Location <span>Map</span></h4>
      <div class="footer-map" role="img" aria-label="Street map of the Sydney area"></div>
    </div>
    <div class="footer-col social">
      <h4>Follow <span>Us</span></h4>
      <div class="social-item"><i></i>News feed</div>
      <div class="social-item"><i></i>Updates</div>
      <div class="social-item"><i></i>Network</div>
      <div class="social-item"><i></i>Circles</div>
    </div>
  </div>
  <div class="copyright">Copyright &copy; 2016 Tidlow Rubbish Removal. All Rights Reserved.</div>
</footer>

</body>
</html>
```